New home maintenance business, on the back of business card i would like dot points of my services provided.
these include,
General household repairs and maintenance
Painting
Plankor/Plaster Repairs
Fencing
Gardening and landscaping
Cleaning and removals
Doors and windows
Hinges and Locks
Fly screen/ screen door Repairs
I like black,silver, red but ill leav it up to you guys as something may be better for business.. , would also it be possible to create a logo for me incorporating the K&T as i want to make up t shirts in future thankyou
Updates
i would also like to put Marco Tessani on the cards aswell please, and on back change painter to proffesional painter and decorator, please
i like alot of the designs sofar, i cant put my finger on wat 1 yet though!! cheers guys
Industry/Entity Type
Business
Contact Information for Business Card
K&T HOME MAINTENANCE SERVICES
Lenny Tessani 0498127654
ktmaintenance@mailvexa.com
ABN:71452038619
Look and feel
Each slider illustrates characteristics of the customer's brand and the style your logo design should communicate.

```html
<!DOCTYPE html>
<html lang="en">
<head>
<meta charset="utf-8">
<title>K&amp;T Home Maintenance Services — Business Card</title>
<link href="https://fonts.googleapis.com/css2?family=Cinzel:wght@700;800&family=Questrial&display=swap" rel="stylesheet">
<style>
  :root {
    --page-bg: #2b2b2d;
    --card-black: #1c1a1b;
    --silver-light: #d9d9db;
    --silver-mid: #a9a9ac;
    --silver-dark: #7d7d80;
    --text-white: #ffffff;
    --text-grey: #b8b8ba;
    --text-soft: #e6e6e6;
    --accent-red: #e0231f;
  }
  * { margin: 0; padding: 0; box-sizing: border-box; }
  html, body {
    width: 1200px; height: 900px; overflow: hidden;
    background: var(--page-bg);
  }
  .sheet {
    position: relative; width: 1200px; height: 900px;
    display: flex; align-items: center; justify-content: center; gap: 40px;
  }
  .card {
    position: relative; width: 540px; height: 330px; overflow: hidden;
    background: linear-gradient(135deg, var(--silver-light), var(--silver-mid) 60%, var(--silver-dark));
    box-shadow: 0 10px 30px rgba(0,0,0,.45);
  }
  .card-shape { position: absolute; inset: 0; width: 100%; height: 100%; }

  /* Front */
  .brand-mark {
    position: absolute; top: 22px; right: 26px;
    display: flex; align-items: center; gap: 8px;
    font-family: "Questrial", sans-serif; font-size: 40px; color: var(--silver-mid);
    line-height: 1;
  }
  .brand-mark .mark-square {
    width: 12px; height: 12px; background: var(--silver-mid);
  }
  .business-name {
    position: absolute; top: 150px; left: 96px;
    font-family: "Cinzel", serif; font-weight: 800; font-size: 18px;
    color: var(--text-white); letter-spacing: 0; white-space: nowrap;
    line-height: 1.2;
  }
  .contact {
    position: absolute; left: 74px; top: 200px;
    font-family: "Questrial", sans-serif; color: var(--text-grey);
    font-size: 18px; line-height: 26px;
  }
  .contact .person { font-weight: 700; color: var(--silver-mid); font-size: 19px; }

  /* Back */
  .services {
    position: absolute; top: 22px; left: 28px;
    font-family: "Questrial", sans-serif;
  }
  .services-title {
    color: var(--accent-red); font-size: 18px; font-weight: 700;
    padding-bottom: 4px; border-bottom: 2px solid var(--silver-dark);
    display: inline-block; padding-right: 60px; margin-bottom: 8px;
  }
  .services-list { list-style: none; padding-left: 28px; }
  .services-list li {
    position: relative; color: var(--text-soft); font-size: 15px; line-height: 28px;
  }
  .services-list li::before {
    content: ""; position: absolute; left: -18px; top: 12px;
    width: 6px; height: 6px; border-radius: 50%; background: var(--text-soft);
  }
</style>
</head>
<body>
<main class="sheet">
  <section class="card card-front" aria-label="Business card front">
    <svg class="card-shape" viewBox="0 0 540 330" preserveAspectRatio="none" aria-hidden="true">
      <path d="M60,330 C30,190 170,30 430,0 L540,0 L540,20 C520,190 420,300 330,330 Z" fill="#8e8e91"/>
      <path d="M40,330 C10,190 150,20 410,0 L540,0 L540,8 C505,180 390,300 290,330 Z" fill="var(--card-black)"/>
    </svg>
    <div class="brand-mark"><span class="mark-square"></span>K&amp;T</div>
    <h1 class="business-name">K&amp;T HOME MAINTENANCE SERVICES</h1>
    <div class="contact">
      <p class="person">Lenny Tessani -</p>
      <p class="phone">049 812 7654</p>
      <p class="email">ktmaintenance@mailvexa.com</p>
      <p class="abn">ABN : 7145 203 8619</p>
    </div>
  </section>

  <section class="card card-back" aria-label="Business card back">
    <svg class="card-shape" viewBox="0 0 540 330" preserveAspectRatio="none" aria-hidden="true">
      <path d="M0,0 L440,0 C560,90 530,250 390,330 L0,330 Z" fill="#8e8e91"/>
      <path d="M0,0 L425,0 C540,90 510,250 370,330 L0,330 Z" fill="var(--card-black)"/>
    </svg>
    <div class="services">
      <h2 class="services-title">Our services</h2>
      <ul class="services-list">
        <li>General household repairs and maintenance</li>
        <li>Painting</li>
        <li>Plankor/Plaster Repairs</li>
        <li>Fencing</li>
        <li>Gardening and landscaping</li>
        <li>Cleaning and removals</li>
        <li>Doors and windows</li>
        <li>Hinges and Locks</li>
        <li>Fly screen/ screen door Repairs</li>
      </ul>
    </div>
  </section>
</main>
</body>
</html>
```